Brightwren Farming

We need a logo design for a new company based in Kelowna, BC. We grow market garden vegetables for sale at market and in a CSA program. We try to only use hand tools for all aspects of cultivating, seeding, weeding, harvesting and distributing. For this reason we consider ourselves very low impact on the environment.

We would like blues and green in the design with an earthy, natural feel

Target Market(s)

Environmentally aware, health conscience

Industry/Entity Type

Farming

Requirements
Must have
• Foot prints with section for contact details all on the one side
Should not have
• Dark, black colours or anything that looks unnatural

```html
<!DOCTYPE html>
<html lang="en">
<head>
<meta charset="utf-8">
<title>Brightwren Farming – Business Card</title>
<link href="https://fonts.googleapis.com/css2?family=Open+Sans:wght@400;600&display=swap" rel="stylesheet">
<style>
  :root {
    --leaf-green: #6bbd45;
    --sky-blue: #1673b6;
    --ink-grey: #6b6b6b;
    --rule-grey: #8a8a8a;
    --paper: #ffffff;
    --backdrop: #eef0ec;
  }
  * { box-sizing: border-box; margin: 0; padding: 0; }
  html, body {
    width: 1200px; height: 1000px; overflow: hidden;
    background: var(--backdrop);
    font-family: "Open Sans", Arial, sans-serif;
  }
  .business-card {
    position: absolute; left: 99px; top: 205px;
    width: 1002px; height: 590px;
    background: var(--paper);
    box-shadow: 0 4px 18px rgba(0,0,0,0.12);
    overflow: hidden;
  }
  .brand-name {
    position: absolute; right: 48px; top: 118px;
    display: flex; align-items: center; gap: 16px;
    font-size: 52px; font-weight: 400; color: var(--leaf-green);
    letter-spacing: 0.5px;
  }
  .brand-dot {
    width: 26px; height: 26px; border-radius: 50%;
    background: var(--sky-blue);
  }
  .name-tab {
    position: absolute; left: 0; top: 292px;
    width: 12px; height: 58px; background: var(--leaf-green);
  }
  .person-name {
    position: absolute; left: 50px; top: 292px;
    font-size: 34px; font-weight: 600; color: var(--leaf-green); line-height: 1.1;
  }
  .person-role {
    position: absolute; left: 50px; top: 334px;
    font-size: 24px; color: var(--ink-grey);
  }
  .divider {
    position: absolute; left: 50px; top: 377px;
    width: 901px; height: 3px; background: var(--rule-grey);
  }
  .contact-list {
    position: absolute; left: 50px; top: 395px;
    list-style: none;
  }
  .contact-list li {
    display: flex; align-items: center; gap: 10px;
    height: 35.5px; font-size: 24px; color: var(--ink-grey);
  }
  .contact-list svg { width: 24px; height: 24px; flex: none; }
  .address {
    position: absolute; right: 48px; top: 430px;
    text-align: right; font-size: 24px; line-height: 35px; color: var(--ink-grey);
    font-style: normal;
  }
  .footer-bands { position: absolute; left: 0; top: 0; }
  .tagline {
    position: absolute; right: 48px; top: 546px;
    font-size: 25px; color: var(--paper); line-height: 40px;
  }
</style>
</head>
<body>
  <main class="business-card">
    <div class="brand-name"><span>Brightwren Farming</span><span class="brand-dot"></span></div>

    <div class="name-tab"></div>
    <h1 class="person-name">Marla Kessington</h1>
    <p class="person-role">Managing Director</p>
    <div class="divider"></div>

    <ul class="contact-list">
      <li>
        <svg viewBox="0 0 24 24"><path fill="var(--leaf-green)" d="M3 9c0-3 4-5 9-5s9 2 9 5l-1 2h-4l-1-2H9l-1 2H4zM6 12h12l2 7H4z"/><circle cx="12" cy="15.5" r="2" fill="#fff"/></svg>
        <span>+ 000 000 0000</span>
      </li>
      <li>
        <svg viewBox="0 0 24 24"><path fill="var(--leaf-green)" d="M7 3h10v5H7zM3 9h18v8h-3v-3H6v3H3zM7 15h10v6H7z"/></svg>
        <span>+ 000 000 0000</span>
      </li>
      <li>
        <svg viewBox="0 0 24 24"><rect x="3" y="6" width="18" height="13" fill="var(--leaf-green)"/><path d="M3 6l9 7 9-7" fill="none" stroke="#fff" stroke-width="1.8"/></svg>
        <span>info@brightwrenfarming.com</span>
      </li>
      <li>
        <svg viewBox="0 0 24 24"><circle cx="12" cy="12" r="9" fill="var(--leaf-green)"/><path d="M3 12h18M12 3c-4 5-4 13 0 18M12 3c4 5 4 13 0 18" fill="none" stroke="#fff" stroke-width="1.4"/></svg>
        <span>www.brightwrenfarming.com</span>
      </li>
    </ul>

    <address class="address">2840 Orchard Bend Road,<br>Kelowna BC V1W 4K2</address>

    <svg class="footer-bands" width="1002" height="590" viewBox="0 0 1002 590" aria-hidden="true">
      <polygon points="0,565 440,565 414,590 0,590" fill="var(--sky-blue)"/>
      <polygon points="472,542 1002,542 1002,590 422,590" fill="var(--leaf-green)"/>
    </svg>
    <p class="tagline">Freshly Picked Food from our Farm</p>
  </main>
</body>
</html>
```